Summer Music/Chorus/Choir Camp for Young Singers Ages 8-13

We need a flyer for a summer camp for young singers ages 8-13. We are nonprofit community children's chorus in Miami, FL. Our camp provides specialized training in music theory, sight-reading,and aural training through daily choral rehearsals in an environment that is both positive and a lot of fun! Our camp offers children the opportunity to come as they are, no matter the level of experience, and grow tremendously in their musicianship skills. In addition to this, our campers participate in song-writing, masterclasses, community performances, and media projects. The final design should be clean, fun, not too crowded, should appeal to boys and girls ages 8-13, and something someone that age would consider "cool" and not too childish. Drawings are cool, something different.
Updates

Target Market(s)

Ages 8-13 and parents of those kids.

Industry/Entity Type

Community

Requirements
Must have
• All info attached.
Nice to have
• Things that relate to music, especially related to singing/choirs
Should not have
• instruments, stock photos of children, or photos from our website (unless they are used very creatively), or photos in general. I've attached our previous camp flyer and our current organization flyer but I don't necessarily want this flyer to look like those.

```html
<!DOCTYPE html>
<html lang="en">
<head>
<meta charset="utf-8">
<title>Summer Camp Flyer</title>
<link href="https://fonts.googleapis.com/css2?family=Permanent+Marker&family=Open+Sans:wght@700;800&display=swap" rel="stylesheet">
<style>
  :root {
    --stage: #3a3a3a;
    --sheet: #2b2b2b;
    --sheet-edge: #6a6a6a;
    --ink: #ffffff;
    --muted: #7a7a7a;
    --accent: #f2b232;
    --rule: #8a8a8a;
    --strip: #ffffff;
    --strip-ink: #1e1e1e;
    --host: #3f8c7d;
  }
  * { margin: 0; padding: 0; box-sizing: border-box; }
  html, body { width: 1200px; height: 1000px; overflow: hidden; background: var(--stage); }
  .canvas { position: relative; width: 1200px; height: 1000px; background: var(--stage); font-family: "Open Sans", Arial, sans-serif; color: var(--ink); }
  .sheet { position: absolute; left: 250px; top: 0; width: 708px; height: 1000px; background: var(--sheet); border: 1px solid var(--sheet-edge); overflow: hidden; }
  .abs { position: absolute; white-space: nowrap; }
  h1, h2 { font-weight: 400; }

  .mic-art { left: 60px; top: 88px; width: 180px; height: 325px; border-radius: 90px 90px 40px 40px;
    background: radial-gradient(ellipse at 50% 35%, #8c8c8c 0%, #4a4a4a 45%, #2b2b2b 80%); }
  .note-art { left: 225px; top: 62px; width: 62px; height: 128px; border-radius: 30px;
    background: linear-gradient(180deg, #e3a92e 0%, #b7811d 100%); opacity: .85; }

  .marker { font-family: "Permanent Marker", "Comic Sans MS", cursive; color: var(--ink); line-height: 1; }
  .headline-love { left: 318px; top: 82px; font-size: 66px; }
  .headline-to { left: 365px; top: 170px; font-size: 66px; }
  .headline-sing { left: 290px; top: 252px; font-size: 66px; }
  .join { left: 516px; top: 308px; font-size: 15px; color: var(--muted); letter-spacing: .5px; }
  .camp-title { left: 110px; top: 428px; font-size: 70px; letter-spacing: 1px; }

  .intro { left: 32px; top: 514px; font-size: 15.4px; line-height: 20.2px; font-weight: 700; }
  .intro .lead { font-size: 19px; }
  .cta { left: 32px; top: 638px; font-size: 19px; font-weight: 700; color: var(--accent); }
  .divider { left: 271px; top: 672px; width: 165px; height: 1px; background: var(--rule); }

  .details { font-size: 12.6px; line-height: 16.4px; font-weight: 700; }
  .hours { left: 30px; top: 766px; }
  .price { left: 30px; top: 848px; }
  .venue { right: 30px; top: 766px; text-align: right; }
  .contact { right: 30px; top: 848px; text-align: right; }
  .label { color: var(--accent); }
  .dots { left: 330px; top: 790px; width: 0; height: 64px; border-left: 2px dotted #555; }

  .footer-strip { left: 0; top: 960px; width: 708px; height: 40px; background: var(--strip); }
  .sponsor { display: flex; align-items: center; gap: 6px; font-size: 14px; font-weight: 800; color: var(--strip-ink); }
  .sponsor .mark { width: 14px; height: 14px; background: var(--strip-ink); }
  .sponsor-left { left: 8px; top: 972px; }
  .sponsor-right { left: 545px; top: 973px; font-size: 11px; }
  .sponsor-right .mark { width: 12px; height: 12px; }
  .badge { left: 665px; top: 962px; width: 36px; height: 36px; border: 2px solid var(--strip-ink); background: #d9d9d9; }
  .host-box { left: 263px; top: 930px; width: 154px; height: 70px; background: var(--strip); display: flex; align-items: center; justify-content: center; }
  .host-name { font-size: 14px; font-weight: 800; color: var(--host); text-align: center; line-height: 16px; }
</style>
</head>
<body>
<div class="canvas">
  <main class="sheet">
    <div class="abs mic-art" role="img" aria-label="Vintage studio microphone illustration"></div>
    <div class="abs note-art" role="img" aria-label="Golden music notes and treble clef"></div>

    <h1>
      <span class="abs marker headline-love">LOVE</span>
      <span class="abs marker headline-to">TO</span>
      <span class="abs marker headline-sing">SING ?</span>
    </h1>
    <p class="abs marker join">COME JOIN US</p>

    <h2 class="abs marker camp-title">SUMMER CAMP</h2>

    <p class="abs intro"><span class="lead">Y</span>outh and children who love to sing will have a blast at our choral camp!<br>Our music educators and industry professionals are dedicated to enhancing the<br>lives of young singers through choral training which develops vocal technique,<br>ear-training, music reading, and interpersonal skills. Activities are fun and<br>interactive and former music training is not necessary.<br>Singers in grades 3-9 are invited to attend!</p>
    <p class="abs cta">Register today!</p>
    <div class="abs divider"></div>

    <p class="abs details hours">OPEN FROM July 18-29, 9am-3pm (M-F)*<br>*Extended hours available<br>(7:30am-5:30pm)<br>for an extra $50 per week.</p>
    <p class="abs details price"><span class="label">FOR JUST</span>&nbsp; *$300 for 2-week session<br>*Price does not include lunch.</p>
    <div class="abs dots"></div>
    <p class="abs details venue">OUR SPACE : Palm Grove Arts Center<br>1420 Harbor View Lane,<br>Bayview, FL 33000</p>
    <p class="abs details contact"><span class="label">CALL US</span> @ 555.014.2200<br>Email- info@skylineyouthchorus.org</p>

    <div class="abs footer-strip"></div>
    <div class="abs sponsor sponsor-left"><span class="mark"></span>Harbor Arts Fund</div>
    <div class="abs host-box"><span class="host-name">Skyline<br>Youth Chorus</span></div>
    <div class="abs sponsor sponsor-right"><span class="mark"></span>Bayshore County</div>
    <div class="abs badge" role="img" aria-label="Partner badge"></div>
  </main>
</div>
</body>
</html>
```